Medical Company in need of a Modern Flyer design for new Wound Care clinic.

Tri-Fold modern flyer design for our Woundcare company. Logo and description of services can be found on our website; https://www.corvin-woundcare.com/

```html
<!DOCTYPE html>
<html lang="en">
<head>
<meta charset="utf-8">
<title>Corvin Woundcare – Tri-Fold Brochure</title>
<link rel="stylesheet" href="https://fonts.googleapis.com/css2?family=Montserrat:wght@400;500;600;700&display=swap">
<style>
  :root{
    --gold:#d9a24a;
    --gold-light:#f0c477;
    --gold-deep:#b7802f;
    --charcoal:#444446;
    --charcoal-dark:#363638;
    --ink:#2f2f31;
    --paper:#ffffff;
    --mist:#f1f1f1;
    --muted:#d8d8d8;
    --body-grey:#5a5a5c;
    --stage:#e3e3e3;
  }
  *{box-sizing:border-box;margin:0;padding:0}
  html,body{width:900px;height:1200px;overflow:hidden}
  body{background:var(--stage);font-family:"Montserrat",Arial,sans-serif;color:var(--ink);position:relative}
  .spread{position:absolute;left:15px;width:870px;height:560px;display:flex;box-shadow:0 6px 18px rgba(0,0,0,.18);background:var(--paper)}
  .spread--outside{top:25px}
  .spread--inside{top:615px}
  .panel{position:relative;width:290px;height:560px;overflow:hidden}
  .panel + .panel{border-left:1px solid rgba(0,0,0,.06)}
  .panel-bg{position:absolute;inset:0;width:290px;height:560px}
  .abs{position:absolute}

  /* outside – services flap */
  .tab-dark{background:var(--charcoal-dark);color:#fff;font-size:14px;font-weight:500;padding:11px 18px;left:22px;top:22px}
  .service-list{left:30px;top:78px;width:240px;list-style:none;font-size:9.5px;line-height:1.3;color:var(--ink)}
  .service-list li{position:relative;padding-left:12px;margin-bottom:4px}
  .service-list li::before{content:"";position:absolute;left:0;top:4px;width:4px;height:4px;background:var(--ink)}
  .feature{left:24px;width:245px;color:#fff}
  .feature-head{display:flex;align-items:center;gap:10px;margin-bottom:6px}
  .feature-icon{width:26px;height:26px;background:linear-gradient(135deg,var(--gold-light),var(--gold-deep));border:2px solid #fff;flex:none}
  .feature-title{font-size:12.5px;font-weight:600;line-height:1.15}
  .feature-body{font-size:8.6px;line-height:1.42;color:#e6e6e6}

  /* outside – contact panel */
  .book-title{left:0;right:0;top:22px;text-align:center;font-size:12.5px;font-weight:600}
  .phone-badge{left:38px;top:44px;display:flex;height:28px}
  .phone-badge .icon{width:30px;background:var(--gold);display:flex;align-items:center;justify-content:center}
  .phone-badge .number{background:#5a5a5c;color:#fff;font-size:17px;font-weight:700;padding:3px 12px;letter-spacing:.5px}
  .web-line{left:0;right:0;top:80px;text-align:center;font-size:12px}
  .web-line b{color:var(--gold-deep);font-weight:600}
  .contact-line{left:0;right:0;text-align:center;font-size:9px;display:flex;justify-content:center;align-items:center;gap:5px}
  .contact-line .pip{width:12px;height:12px;background:var(--gold);display:inline-flex;align-items:center;justify-content:center}
  .photo-lobby{left:0;top:150px;width:290px;height:240px;background:linear-gradient(160deg,#f4f4f2 0%,#cfd4d6 35%,#8fa7b3 55%,#d9cfbf 80%,#efe9e0 100%)}
  .plans-box{left:18px;top:410px;width:254px;height:86px;border:1px solid #777;border-radius:10px}
  .plans-legend{left:0;right:0;top:-8px;text-align:center}
  .plans-legend span{background:#fff;padding:0 8px;font-size:10px;font-weight:600}
  .plan-badges{left:14px;right:14px;top:18px;display:flex;flex-wrap:wrap;justify-content:space-around;gap:8px 10px}
  .plan-badge{width:60px;height:20px;border-radius:4px;background:#c9d0d6}
  .plans-note{left:22px;width:246px;top:506px;font-size:7.5px;line-height:1.4;text-align:center;color:var(--body-grey)}

  /* outside – cover */
  .brand{left:0;right:0;top:38px;display:flex;flex-direction:column;align-items:center;gap:10px}
  .brand-mark{width:22px;height:22px;background:var(--gold)}
  .brand-name{font-size:15px;font-weight:500;letter-spacing:4px;color:var(--ink)}
  .photo-cover{left:0;top:110px;width:290px;height:270px;background:linear-gradient(170deg,#e9eaea 0%,#b7bec2 40%,#7e9aa6 60%,#d5d2cc 85%,#f2efe9 100%)}
  .cover-title{left:0;right:0;top:408px;text-align:center;font-size:23px;font-weight:500;line-height:1.15;color:var(--ink)}
  .cover-text{left:40px;width:210px;top:470px;text-align:center;font-size:8.5px;line-height:1.4;color:var(--ink)}
  .cover-web{left:0;right:0;top:518px;text-align:center;font-size:12px;color:var(--ink)}
  .cover-web b{font-weight:600}

  /* inside – wound types */
  .photo-chamber{left:0;top:0;width:290px;height:205px;background:linear-gradient(150deg,#f1f1ef 0%,#cfd2d3 40%,#9ea5aa 65%,#e5e3df 100%)}
  .tab-gold{background:linear-gradient(90deg,var(--gold-light),var(--gold));color:var(--ink);font-size:14px;font-weight:500;padding:10px 18px}
  .tab-types{left:22px;top:200px}
  .type-cols{left:24px;top:250px;width:256px;display:flex;gap:12px}
  .type-list{list-style:none;font-size:9px;line-height:1.2;color:#fff}
  .type-list--a{width:104px;white-space:nowrap}
  .type-list--b{width:136px}
  .type-list li{position:relative;padding-left:11px;margin-bottom:3px}
  .type-list li::before{content:"";position:absolute;left:0;top:4px;width:4px;height:4px;background:var(--gold)}
  .types-text{left:24px;width:248px;top:362px;font-size:8.3px;line-height:1.42;color:#fff;text-align:justify}

  /* inside – HBO panel */
  .hbo{left:22px;width:250px;color:var(--ink)}
  .hbo h2{font-size:14px;font-weight:600;line-height:1.2;margin-bottom:8px}
  .hbo p{font-size:8.8px;line-height:1.45;text-align:justify;color:#3b3326}

  /* inside – treatment panel */
  .tab-treat{left:20px;top:22px}
  .treat-list{left:28px;top:78px;width:245px;list-style:none;font-size:9.3px;line-height:1.25;color:var(--ink)}
  .treat-list li{position:relative;padding-left:11px;margin-bottom:2px}
  .treat-list li::before{content:"";position:absolute;left:0;top:4px;width:4px;height:4px;background:var(--gold)}
  .treat-text{left:24px;width:246px;top:222px;font-size:8.6px;line-height:1.42;color:var(--body-grey);text-align:justify}
  .photo-care{left:0;top:392px;width:290px;height:168px;background:linear-gradient(135deg,#f4f6f8 0%,#dfe4ea 40%,#e9d4c6 70%,#c99a88 100%)}
</style>
</head>
<body>

<section class="spread spread--outside">

  <article class="panel panel-services">
    <svg class="panel-bg" viewBox="0 0 290 560" aria-hidden="true">
      <defs>
        <linearGradient id="goldA" x1="0" y1="0" x2="1" y2="1">
          <stop offset="0" stop-color="#f0c477"/><stop offset="1" stop-color="#c98f3a"/>
        </linearGradient>
      </defs>
      <rect width="290" height="560" fill="#444446"/>
      <path d="M0 0H290V160Q160 190 0 212Z" fill="url(#goldA)"/>
      <path d="M0 553Q150 547 290 526V532Q150 553 0 559Z" fill="#d9a24a"/>
    </svg>
    <div class="abs tab-dark">Our Services</div>
    <ul class="abs service-list">
      <li>Hyperbaric Oxygen Therapy (HBO): A Cornerstone of Advanced Wound Care</li>
      <li>Debridement</li>
      <li>Advanced Wound Dressings</li>
      <li>Bio-engineered Skin Substitutes</li>
      <li>Compression Therapy and Edema Management</li>
    </ul>
    <div class="abs feature" style="top:226px">
      <div class="feature-head"><span class="feature-icon"></span><span class="feature-title">Accepted<br>Health Plans</span></div>
      <p class="feature-body">We accept most major insurance plans to make your care as accessible and affordable as possible!</p>
    </div>
    <div class="abs feature" style="top:304px">
      <div class="feature-head"><span class="feature-icon"></span><span class="feature-title">Expert<br>Medical Team</span></div>
      <p class="feature-body">Comprised of highly trained physicians, nurses, and specialists, our team brings years of experience in treating a wide range of complex wounds. With a commitment to innovative treatments and personalized care plans, we work closely with each patient to ensure optimal healing and recovery. Trust our team to provide the expert care you need for lasting results.</p>
    </div>
    <div class="abs feature" style="top:448px">
      <div class="feature-head"><span class="feature-icon"></span><span class="feature-title">Trusted<br>Healthcare Provider</span></div>
      <p class="feature-body">We specialize in advanced treatment modalities, using a multi-faceted approach to heal your patient's wound.</p>
    </div>
  </article>

  <article class="panel panel-contact">
    <h3 class="abs book-title">Book Your Appointment Online</h3>
    <div class="abs phone-badge">
      <span class="icon">
        <svg width="14" height="14" viewBox="0 0 24 24" aria-hidden="true"><path fill="#2f2f31" d="M6.6 10.8a15.1 15.1 0 0 0 6.6 6.6l2.2-2.2c.3-.3.7-.4 1-.2 1.1.4 2.3.6 3.6.6.6 0 1 .4 1 1V20c0 .6-.4 1-1 1C10.6 21 3 13.4 3 4c0-.6.4-1 1-1h3.5c.6 0 1 .4 1 1 0 1.3.2 2.5.6 3.6.1.3 0 .7-.2 1z"/></svg>
      </span>
      <span class="number">555-014-2290</span>
    </div>
    <p class="abs web-line">www.<b>corvin-woundcare</b>.com</p>
    <p class="abs contact-line" style="top:104px">
      <span class="pip"><svg width="8" height="8" viewBox="0 0 24 24" aria-hidden="true"><path fill="#2f2f31" d="M12 2a7 7 0 0 0-7 7c0 5 7 13 7 13s7-8 7-13a7 7 0 0 0-7-7zm0 9.5A2.5 2.5 0 1 1 12 6.5a2.5 2.5 0 0 1 0 5z"/></svg></span>
      4120 Meadow Lane Bldg. C, Suite 210
    </p>
    <p class="abs contact-line" style="top:124px">
      <span class="pip"><svg width="8" height="8" viewBox="0 0 24 24" aria-hidden="true"><rect x="4" y="9" width="16" height="11" fill="#2f2f31"/><rect x="7" y="3" width="10" height="6" fill="#2f2f31"/></svg></span>
      555-014-2291
    </p>
    <div class="abs photo-lobby" role="img" aria-label="Bright modern clinic lobby with blue lounge chairs, plants and large windows"></div>
    <svg class="abs" style="left:0;top:370px" width="290" height="40" viewBox="0 0 290 40" aria-hidden="true"><path d="M0 40V20Q150 0 290 30V40Z" fill="#fff"/></svg>
    <div class="abs plans-box">
      <div class="abs plans-legend"><span>Accepted Health Plans</span></div>
      <div class="abs plan-badges">
        <span class="plan-badge"></span><span class="plan-badge"></span><span class="plan-badge"></span>
        <span class="plan-badge"></span><span class="plan-badge"></span>
      </div>
    </div>
    <p class="abs plans-note">At My Site, we accept a variety of health insurance plans to ensure that you receive the care you need. If your current plan is not listed, please get in touch with us so we can explore alternative options that best suit your needs.</p>
  </article>

  <article class="panel panel-cover">
    <svg class="panel-bg" viewBox="0 0 290 560" aria-hidden="true">
      <defs>
        <linearGradient id="goldB" x1="0" y1="0" x2="1" y2="1">
          <stop offset="0" stop-color="#f0c477"/><stop offset="1" stop-color="#c98f3a"/>
        </linearGradient>
      </defs>
      <rect width="290" height="560" fill="#f4f4f4"/>
      <path d="M0 395Q150 375 290 350V560H0Z" fill="url(#goldB)"/>
    </svg>
    <div class="abs brand">
      <span class="brand-mark"></span>
      <span class="brand-name">CORVIN WOUNDCARE</span>
    </div>
    <div class="abs photo-cover" role="img" aria-label="Spacious clinic waiting area with white seating, plants and tall windows"></div>
    <svg class="abs" style="left:0;top:340px" width="290" height="60" viewBox="0 0 290 60" aria-hidden="true">
      <defs><linearGradient id="goldC" x1="0" y1="0" x2="1" y2="1"><stop offset="0" stop-color="#f0c477"/><stop offset="1" stop-color="#c98f3a"/></linearGradient></defs>
      <path d="M0 60V55Q150 35 290 10V60Z" fill="url(#goldC)"/>
    </svg>
    <h1 class="abs cover-title">Caring for Your<br>Well-being</h1>
    <p class="abs cover-text">At Corvin Woundcare, we specialize in managing outpatient wound care facilities throughout the Dallas/Fort Worth area.</p>
    <p class="abs cover-web">www.<b>corvin-woundcare</b>.com</p>
  </article>
</section>

<section class="spread spread--inside">

  <article class="panel panel-types">
    <svg class="panel-bg" viewBox="0 0 290 560" aria-hidden="true">
      <rect width="290" height="560" fill="#444446"/>
      <path d="M0 552Q150 544 290 526V532Q150 550 0 558Z" fill="#d9a24a"/>
    </svg>
    <div class="abs photo-chamber" role="img" aria-label="Clear hyperbaric oxygen chamber with a padded bed in a white treatment room"></div>
    <svg class="abs" style="left:0;top:170px" width="290" height="40" viewBox="0 0 290 40" aria-hidden="true"><path d="M0 40V30Q150 25 290 0V40Z" fill="#444446"/></svg>
    <div class="abs tab-gold tab-types">Wound Types</div>
    <div class="abs type-cols">
      <ul class="type-list type-list--a">
        <li>Atypical Wounds</li><li>Bone Infections</li><li>Burn Wounds</li>
        <li>Chronic Wounds</li><li>Diabetic Ulcers</li><li>Diabetic Wounds</li><li>Infected Wounds</li>
      </ul>
      <ul class="type-list type-list--b">
        <li>Pressure Ulcers</li><li>Venous Leg Ulcers</li><li>Venous &amp; Arterial Ulcers</li>
        <li>Surgical Wound Complications</li><li>Non-Healing Surgical Wounds</li>
      </ul>
    </div>
    <p class="abs types-text">At Corvin Woundcare we specialize in treating a wide range of complex and hard-to-heal wounds. Our expert team is equipped to care for atypical wounds, bone infections, burn wounds, chronic wounds, and diabetic ulcers. We also provide advanced care for non-healing surgical wounds, infected wounds, pilonidal cysts, pressure ulcers, and surgical wound complications. Additionally, we treat venous and arterial ulcers, including venous leg ulcers, using the latest techniques and personalized care plans to promote healing and prevent complications. No matter the wound type, our focus is on achieving optimal outcomes for every patient.</p>
  </article>

  <article class="panel panel-hbo">
    <svg class="panel-bg" viewBox="0 0 290 560" aria-hidden="true">
      <defs>
        <linearGradient id="goldD" x1="0" y1="0" x2="1" y2="1">
          <stop offset="0" stop-color="#f3c983"/><stop offset=".5" stop-color="#dba553"/><stop offset="1" stop-color="#c48b3a"/>
        </linearGradient>
      </defs>
      <rect width="290" height="560" fill="url(#goldD)"/>
    </svg>
    <div class="abs hbo" style="top:24px">
      <h2>Hyperbaric Oxygen Therapy: A Cornerstone of Advanced Wound Care</h2>
      <p>Hyperbaric Oxygen Therapy (HBO) is not just a treatment; it's a pivotal part of our comprehensive approach to wound healing at Corvin Woundcare. By delivering pure oxygen in a pressurized chamber, HBO therapy significantly increases the amount of oxygen in the blood, fostering an environment that accelerates the repair and regeneration of wounded tissues.</p>
    </div>
    <div class="abs hbo" style="top:178px">
      <h2>How HBO Benefits<br>Wound Healing:</h2>
      <p>Enhanced Oxygen Supply: Increases the oxygen level in blood and tissues, which is crucial for healing damaged cells. Stimulation of New Blood Vessels: Encourages the formation of new blood vessels, improving blood flow to areas with impaired circulation. Enhanced White Blood Cell Action: Aids the body's immune system in fighting infection and bacteria at the wound site. Reduction of Swelling and Inflammation: Speeds up healing processes and reduces pain by decreasing swelling and inflammation. Fibroblast Activation: Promotes collagen production, which is vital for wound closure and strength.</p>
    </div>
    <div class="abs hbo" style="top:390px">
      <h2>How HBO Benefits<br>Wound Healing:</h2>
      <p>Chronic Wounds: Especially effective in treating non-healing wounds that have not improved with other treatments. Infections: Including bone infections (osteomyelitis) and diabetic foot ulcers. Crush Injuries and Radiation Injuries: Reduces swelling and improves oxygen supply to tissues that have been compromised. Skin Grafts and Flaps: Ensures the survival of these tissues by enhancing oxygenation and vascular growth.</p>
    </div>
  </article>

  <article class="panel panel-treatment">
    <svg class="panel-bg" viewBox="0 0 290 560" aria-hidden="true">
      <rect width="290" height="560" fill="#ffffff"/>
    </svg>
    <div class="abs tab-gold tab-treat">Wound Treatment</div>
    <ul class="abs treat-list">
      <li>Compression Therapy</li>
      <li>Mechanical &amp; Enzymatic Debridement</li>
      <li>Negative Pressure Wound Therapy</li>
      <li>Post-Mohs Surgery</li>
      <li>Tissue Infection Management / Labs</li>
      <li>Total Contact Casting</li>
      <li>Wound Care</li>
      <li>Wound Debridement</li>
    </ul>
    <p class="abs treat-text">At Corvin Woundcare we offer a full spectrum of advanced wound care treatments designed to promote healing and improve patient outcomes. Our treatments include compression therapy, mechanical and enzymatic debridement, and negative pressure wound therapy to help manage and accelerate wound healing. We also specialize in post-Mohs surgery care, tissue infection management with onsite labs, and total contact casting for diabetic foot ulcers. Whether you need wound debridement or comprehensive wound care, our expert team is here to provide personalized treatments for faster recovery and lasting results.</p>
    <div class="abs photo-care" role="img" aria-label="Clinician wrapping a white bandage around a patient's knee"></div>
  </article>
</section>

</body>
</html>
```